Ductless Mini Split Business Website

Amber Kite Services is looking to design an eye catching educational website about installing Ductless mini splits.

Similar to this company.
https://www.cedarcoolair.com/

```html
<!DOCTYPE html>
<html lang="en">
<head>
<meta charset="utf-8">
<title>Amber Kite Services – Ductless Experts</title>
<link rel="stylesheet" href="https://fonts.googleapis.com/css2?family=Rubik:wght@400;500;700&family=Roboto:wght@400;500;700&display=swap">
<style>
:root{
  --yellow:#f9c41b;
  --ink:#222222;
  --text:#555555;
  --muted:#8a8a8a;
  --line:#e6e6e6;
  --soft:#f6f6f6;
  --footer:#232323;
  --white:#ffffff;
}
*{box-sizing:border-box;margin:0;padding:0}
html,body{width:1200px;height:5159px;overflow:hidden}
body{position:relative;background:var(--white);font-family:'Roboto',sans-serif;color:var(--text)}
.abs{position:absolute}
.hl{color:var(--yellow)}
.label{position:absolute;font:700 13px/1 'Rubik',sans-serif;letter-spacing:2px;color:var(--ink);display:flex;align-items:center;gap:14px}
.label::after{content:"";display:block;width:76px;height:1px;background:var(--ink)}
.h2{position:absolute;font:700 35px/1.3 'Rubik',sans-serif;color:var(--ink)}
.btn{position:absolute;background:var(--yellow);border-radius:24px;font:500 11px/1 'Roboto',sans-serif;letter-spacing:1px;color:var(--ink);display:flex;align-items:center;justify-content:center;text-transform:uppercase}
.photo{position:absolute}
p.body{position:absolute;font:400 12px/22px 'Roboto',sans-serif;color:var(--muted)}

/* header */
.topbar{position:absolute;top:0;left:0;width:1200px;height:84px;border-bottom:1px solid var(--line);background:var(--white)}
.topbar .contact{position:absolute;top:7px;font-size:11px;color:var(--muted);display:flex;align-items:center;gap:8px}
.social{position:absolute;display:flex;gap:6px}
.social span{width:20px;height:20px;border:1px solid #999;border-radius:50%}
.brand{position:absolute;left:500px;top:0;width:200px;height:70px;background:var(--white);display:flex;align-items:center;justify-content:center;gap:8px;font:700 17px/1.1 'Rubik',sans-serif;color:var(--ink);text-align:center}
.brand i{display:block;width:14px;height:14px;border-radius:50%;background:var(--yellow)}
.nav a{position:absolute;top:56px;font:400 11px/1 'Roboto',sans-serif;color:var(--ink);text-decoration:none;letter-spacing:.5px}
.nav a.active{color:var(--yellow)}

/* hero */
.hero-title{position:absolute;left:138px;top:282px;font:700 44px/50px 'Rubik',sans-serif;color:var(--white)}
.hero-sub{position:absolute;left:140px;top:396px;font:500 14px/1 'Roboto',sans-serif;color:var(--white)}

/* services */
.card{position:absolute;width:294px;height:316px;background:var(--white);box-shadow:0 3px 12px rgba(0,0,0,.12)}
.card .img{height:228px}
.card h3{height:88px;display:flex;align-items:center;justify-content:center;text-align:center;font:500 12px/22px 'Rubik',sans-serif;letter-spacing:1.2px;color:var(--ink);text-transform:uppercase}

/* features */
.feat{position:absolute;left:600px;display:flex;gap:20px}
.feat h4{font:400 19px/1 'Rubik',sans-serif;color:var(--ink);margin:2px 0 10px}
.feat p{font-size:11px;line-height:20px;color:var(--muted);width:270px}

/* testimonial */
.quote-card{position:absolute;left:136px;top:3078px;width:928px;height:222px;background:var(--white);box-shadow:0 2px 14px rgba(0,0,0,.1)}

/* faq */
.faq-item{position:absolute;left:608px;width:456px;height:42px;background:var(--white);box-shadow:0 1px 8px rgba(0,0,0,.1);display:flex;align-items:center;justify-content:space-between;padding:0 18px;font-size:11px;color:var(--ink)}
.faq-item b{width:14px;height:14px;border:1px solid #999;border-radius:50%;font:400 11px/12px 'Roboto',sans-serif;text-align:center}
.faq-item.open{background:var(--yellow);color:var(--white)}
.faq-item.open b{border-color:var(--white);background:var(--white);color:var(--yellow)}

/* contact form */
.field{position:absolute;border-bottom:1px solid var(--line);font-size:11px;color:var(--muted);padding-bottom:12px}

/* footer */
.footer{position:absolute;left:0;top:4808px;width:1200px;height:351px;background:var(--footer)}
.footer h5{position:absolute;font:500 14px/1 'Rubik',sans-serif;letter-spacing:2px;color:var(--white)}
.footer ul{position:absolute;list-style:none;font-size:11px;line-height:28px;color:#bbbbbb}
.footer .social span{border-color:#bbbbbb}
</style>
</head>
<body>

<!-- Header -->
<header class="topbar">
  <div class="contact" style="left:136px">
    <svg width="14" height="14" viewBox="0 0 14 14"><circle cx="7" cy="7" r="7" fill="#f9c41b"/><path d="M4.5 4c.6 2.6 2.5 4.6 5 5.4l.8-1-1.4-.8-.6.6c-1-.6-1.7-1.3-2.2-2.3l.6-.6-.8-1.4z" fill="#fff"/></svg>
    Call : (555) 014 2290
  </div>
  <div class="contact" style="left:758px">
    <svg width="14" height="10" viewBox="0 0 14 10"><rect width="14" height="10" rx="1" fill="#f9c41b"/><path d="M1 1l6 5 6-5" stroke="#fff" fill="none"/></svg>
    info@amberkiteservices.com
  </div>
  <div class="social" style="left:958px;top:2px"><span></span><span></span><span></span><span></span></div>
  <div class="brand"><i></i>Amber Kite<br>Services</div>
  <nav class="nav">
    <a class="active" style="left:140px">HOME</a>
    <a style="left:245px">ABOUT US</a>
    <a style="left:362px">SERVICES</a>
    <a style="left:760px">FINANCE</a>
    <a style="left:880px">REVIEWS</a>
    <a style="left:990px">CONTACT US</a>
  </nav>
</header>

<!-- Hero -->
<section>
  <div class="photo" role="img" aria-label="Woman in a bright brick-walled office adjusting a wall-mounted ductless air conditioner with a remote" style="left:0;top:85px;width:1200px;height:597px;background:linear-gradient(90deg,#6d6b68 0%,#8e8b87 40%,#a5a19b 70%,#7c7975 100%)"></div>
  <h1 class="hero-title">Ductless Does It<br><span class="hl">Better</span></h1>
  <div class="hero-sub">Lorem ipsum dolor sit amet, eius impetus et mel ubique</div>
  <div class="btn" style="left:138px;top:437px;width:143px;height:40px">Contact Us</div>
</section>

<!-- About -->
<section>
  <div class="label" style="left:136px;top:807px">ABOUT AMBER KITE SERVICES</div>
  <h2 class="h2" style="left:136px;top:850px">We Are <span class="hl">Leader</span> in the<br>Ductless Area</h2>
  <p class="body" style="left:136px;top:965px;width:490px">Lorem ipsum dolor sit amet, eius impetus et mel. Ubique facilisis has at. Usu ceteros voluptatum at, sea dicit euripidis reprimique ea. Id sea quaeque appareat voluptatibus, wisi splendide per cu. Purto maluisset disputationi cu eos.</p>
  <p class="body" style="left:136px;top:1060px;width:490px">Mei an iracundia consequat, cu agam cetero has, saperet partiendo posidonium mea ne. Sed idque persequeris accommodare cu. Eu imperdiet assueverit appellantur sea. Debet viderer appetere te duo, alii legimus suavitate pro ea. Te has dicat ceteros me-diocrem, nec an luptatum praesent. Legere legimus fabellas in nam, exerci tempor ermod no eum.</p>
  <p class="abs" style="left:136px;top:1200px;width:400px;font:500 14px/23px 'Roboto',sans-serif;color:var(--ink)">Call us at <span class="hl">555.014.2290</span> or click here to schedule a free consultation.</p>
  <div class="photo" role="img" aria-label="Family relaxing on a sofa beneath a wall-mounted ductless unit" style="left:692px;top:808px;width:370px;height:440px;background:linear-gradient(180deg,#f1f1f1 0%,#e2e2e0 55%,#c9c6c0 100%)"></div>
  <svg class="abs" style="left:730px;top:1145px" width="54" height="54" viewBox="0 0 54 54"><circle cx="27" cy="27" r="26" fill="#fff" opacity=".5"/><circle cx="27" cy="27" r="20" fill="#f9c41b"/><path d="M23 19l11 8-11 8z" fill="#fff"/></svg>
  <div class="abs" style="left:806px;top:1164px;font:500 12px/1 'Roboto',sans-serif;color:var(--white);letter-spacing:1px">WATCH VIDEO</div>
</section>

<!-- Services -->
<section>
  <div class="abs" style="left:0;top:1396px;width:1200px;text-align:center;font:700 13px/1 'Rubik',sans-serif;letter-spacing:2px;color:var(--ink)">HOW CAN WE HELP YOU?</div>
  <div class="abs" style="left:560px;top:1430px;width:80px;height:2px;background:var(--ink)"></div>

  <article class="card" style="left:136px;top:1496px"><div class="img" role="img" aria-label="Technician servicing an indoor wall unit" style="background:linear-gradient(180deg,#eceae6,#cfcac2)"></div><h3>Baseboard Heat<br>Replacemant</h3></article>
  <article class="card" style="left:453px;top:1496px"><div class="img" role="img" aria-label="Bright bedroom with a ductless unit above the bed" style="background:linear-gradient(180deg,#f0eeea,#b9b4ad)"></div><h3>Ductless for Addiction &amp;<br>Remodeling</h3></article>
  <article class="card" style="left:771px;top:1496px"><div class="img" role="img" aria-label="Installer wiring a wall-mounted air conditioner" style="background:linear-gradient(180deg,#9a9893,#6f6c68)"></div><h3>Ductless<br>Installation</h3></article>
  <article class="card" style="left:136px;top:1838px"><div class="img" role="img" aria-label="Living room with dark wall unit above a white sofa" style="background:linear-gradient(180deg,#f2f1ef,#c8c5c0)"></div><h3>Whole House<br>Ductless</h3></article>
  <article class="card" style="left:453px;top:1838px"><div class="img" role="img" aria-label="Woman on a sofa using a remote under a ductless unit" style="background:linear-gradient(180deg,#e9e8e6,#a8b4c8)"></div><h3>Ductless for Addiction &amp;<br>Remodeling</h3></article>
  <article class="card" style="left:771px;top:1838px"><div class="img" role="img" aria-label="Woman in a white dining room holding a remote" style="background:linear-gradient(180deg,#f1f1ef,#8d9aa8)"></div><h3>Ductless<br>Installation</h3></article>

  <div class="btn" style="left:501px;top:2191px;width:199px;height:44px">View All Services</div>
</section>

<!-- Features -->
<section>
  <div class="photo" role="img" aria-label="Woman pointing a remote at a ductless unit on a white brick wall" style="left:0;top:2366px;width:508px;height:616px;background:linear-gradient(90deg,#d9d8d5,#efeeec 60%,#cfcdc9)"></div>
  <div class="abs" style="left:508px;top:2366px;width:692px;height:616px;background:var(--soft)"></div>
  <div class="label" style="left:602px;top:2460px">FEATURES</div>
  <h2 class="h2" style="left:602px;top:2500px">Why <span class="hl">Choose</span> Amber Kite<br>Heros?</h2>

  <div class="feat" style="top:2630px">
    <svg width="44" height="50" viewBox="0 0 44 50"><circle cx="22" cy="22" r="19" fill="none" stroke="#222" stroke-width="2"/><circle cx="22" cy="22" r="13" fill="#f9c41b"/><path d="M14 43l-3 6 6-2M30 43l3 6-6-2" stroke="#222" stroke-width="2" fill="none"/><path d="M17 21h4v8h-4zM21 22l3-6h2v5h4l-1 8h-8" fill="#fff" stroke="#222" stroke-width="1.5"/></svg>
    <div><h4>Quality</h4><p>Lorem ipsum dolor sit amet, eius impetus et mel. Ubique facilisis has at.</p></div>
  </div>
  <div class="feat" style="top:2722px">
    <svg width="44" height="50" viewBox="0 0 44 50"><path d="M10 14h24l6 32H4z" fill="none" stroke="#222" stroke-width="2"/><path d="M16 14a6 6 0 0112 0" fill="none" stroke="#222" stroke-width="2"/><circle cx="22" cy="32" r="9" fill="#f9c41b"/><text x="22" y="37" font-size="13" text-anchor="middle" font-family="Roboto,sans-serif" font-weight="700" fill="#222">$</text></svg>
    <div><h4>Great Price</h4><p>We keep our prices and shipping cost as low as possible for our customers.</p></div>
  </div>
  <div class="feat" style="top:2818px">
    <svg width="44" height="50" viewBox="0 0 44 50"><path d="M13 22v-7a9 9 0 0118 0v7" fill="none" stroke="#222" stroke-width="2"/><rect x="7" y="22" width="30" height="24" rx="3" fill="none" stroke="#222" stroke-width="2"/><circle cx="22" cy="32" r="4" fill="#f9c41b"/><path d="M22 35v5" stroke="#222" stroke-width="2"/></svg>
    <div><h4>Secure</h4><p>Shop safely with encrypted protection, we will never share your info with anyone.</p></div>
  </div>
</section>

<!-- Testimonial -->
<section class="quote-card">
  <div class="abs" role="img" aria-label="Customer portrait" style="left:50px;top:46px;width:64px;height:64px;border-radius:50%;background:linear-gradient(135deg,#d7c6bd,#8b7a74)"></div>
  <svg class="abs" style="left:62px;top:162px" width="40" height="8" viewBox="0 0 40 8"><circle cx="4" cy="4" r="4" fill="#f9c41b"/><circle cx="20" cy="4" r="3.5" fill="none" stroke="#ccc"/><circle cx="36" cy="4" r="3.5" fill="none" stroke="#ccc"/></svg>
  <div class="abs" style="left:212px;top:48px;font:500 14px/1 'Roboto',sans-serif;color:var(--ink)">Oh, my gosh! These guys are awesome.</div>
  <p class="body" style="left:212px;top:78px;width:540px">Lorem ipsum dolor sit amet, eius impetus et mel. Ubique facilisis has at. Usu ceteros voluptatum at, sea dicit euripidis reprimique ea.</p>
  <div class="abs" style="left:212px;top:154px;font:500 13px/1 'Roboto',sans-serif;letter-spacing:1px;color:var(--yellow)">MARA LENTZ</div>
  <div class="abs" style="left:212px;top:174px;font-size:10px;color:var(--muted)">Investment Manager</div>
  <div class="abs" style="left:842px;top:20px;font:700 72px/1 'Rubik',sans-serif;color:#e4e4e4">&rdquo;</div>
</section>

<!-- FAQ -->
<section>
  <div class="label" style="left:136px;top:3382px">FAQs</div>
  <h2 class="h2" style="left:136px;top:3422px;font-size:32px">We <span class="hl">respond</span> to all inquiries<br>received</h2>
  <div class="btn" style="left:136px;top:3558px;width:193px;height:42px">Send for Request</div>
  <div class="faq-item" style="top:3378px">What Are Good Billing Methods?<b>+</b></div>
  <div class="faq-item open" style="top:3440px">Collecting Debt Collection for All Businesses?<b>+</b></div>
  <div class="faq-item" style="top:3499px">What is the cost of the claimant?<b>+</b></div>
  <div class="faq-item" style="top:3557px">What is the cost of the claimant?<b>+</b></div>
</section>

<!-- News -->
<section>
  <div class="abs" style="left:0;top:3712px;width:748px;height:484px;background:var(--soft)"></div>
  <div class="photo" role="img" aria-label="Grey bedroom with pendant lights and a wall-mounted ductless unit" style="left:748px;top:3712px;width:452px;height:484px;background:linear-gradient(180deg,#8a8f92 0%,#7d8285 60%,#9a8d7c 100%)"></div>
  <div class="label" style="left:136px;top:3800px">NEWS</div>
  <h2 class="h2" style="left:136px;top:3842px">Latest <span class="hl">Blog</span> &amp; Post</h2>
  <div class="abs" style="left:136px;top:3922px;font-size:10px;color:var(--muted);display:flex;gap:10px;align-items:center"><svg width="12" height="11" viewBox="0 0 12 11"><rect x=".5" y="1.5" width="11" height="9" fill="none" stroke="#f9c41b"/><path d="M.5 4h11" stroke="#f9c41b"/></svg>25 DEC 2019</div>
  <div class="abs" style="left:136px;top:3960px;width:400px;font:400 17px/27px 'Roboto',sans-serif;color:var(--ink)">Thoughts On Buying Property Ahead Of A Potential Recession</div>
  <p class="body" style="left:136px;top:4028px;width:420px">Lorem ipsum dolor sit amet, eius impetus et mel. Ubique facilisis has at. Usu ceteros voluptatum at, sea dicit euripidis reprimique ea. Id sea quae-que appareat voluptatibu</p>
  <div class="abs" style="left:134px;top:4130px;font:700 64px/1 'Rubik',sans-serif;color:#ececec">01</div>
  <div class="abs" style="left:682px;top:4136px;width:66px;height:60px;background:var(--ink);display:flex;align-items:center;justify-content:center"><svg width="20" height="10" viewBox="0 0 20 10"><path d="M20 5H2M6 1L2 5l4 4" stroke="#fff" stroke-width="1.5" fill="none"/></svg></div>
  <div class="abs" style="left:748px;top:4136px;width:66px;height:60px;background:var(--yellow);display:flex;align-items:center;justify-content:center"><svg width="20" height="10" viewBox="0 0 20 10"><path d="M0 5h18M14 1l4 4-4 4" stroke="#fff" stroke-width="1.5" fill="none"/></svg></div>
</section>

<!-- Contact -->
<section>
  <div class="label" style="left:136px;top:4344px">CONTACT US</div>
  <h2 class="h2" style="left:136px;top:4386px;line-height:52px">We're <span class="hl">always</span><br>ready to discuss<br>coperation</h2>
  <div class="abs" style="left:136px;top:4580px;display:flex;gap:24px;font-size:12px;line-height:22px"><svg width="12" height="16" viewBox="0 0 12 16"><path d="M6 15S1 9 1 6a5 5 0 0110 0c0 3-5 9-5 9z" fill="none" stroke="#f9c41b" stroke-width="1.5"/><circle cx="6" cy="6" r="2" fill="#f9c41b"/></svg><span>418 Larkspur Ridge Rd, Ste 210<br>Fernvale, NV 89120</span></div>
  <div class="abs" style="left:136px;top:4636px;display:flex;gap:24px;font-size:13px;color:var(--ink)"><svg width="12" height="12" viewBox="0 0 12 12"><path d="M1 1c1 5 4 9 10 10l1-3-3-1-1 1C6 7 5 6 4 4l1-1-1-3z" fill="#f9c41b"/></svg>555.014.3381</div>
  <div class="abs" style="left:136px;top:4678px;display:flex;gap:24px;font-size:12px;color:#2a7fd4"><svg width="12" height="9" viewBox="0 0 12 9"><rect width="12" height="9" fill="#f9c41b"/><path d="M0 0l6 5 6-5" stroke="#fff" fill="none"/></svg>info@amberkiteservices.com</div>

  <div class="abs" style="left:584px;top:4346px;font:400 18px/1 'Roboto',sans-serif;color:var(--ink)">I would like to discuss:</div>
  <div class="field" style="left:584px;top:4402px;width:224px">Name*</div>
  <div class="field" style="left:840px;top:4402px;width:224px">Last Name*</div>
  <div class="field" style="left:584px;top:4454px;width:224px">Phone*</div>
  <div class="field" style="left:840px;top:4454px;width:224px">Email*</div>
  <div class="field" style="left:584px;top:4506px;width:480px;display:flex;justify-content:space-between">Are You A Customer<span>&#9662;</span></div>
  <div class="field" style="left:584px;top:4562px;width:480px;height:60px">Message</div>
  <div class="btn" style="left:584px;top:4656px;width:176px;height:40px;letter-spacing:2px;font-weight:700">Send Message &nbsp;&#8250;</div>
</section>

<!-- Footer -->
<footer class="footer">
  <div class="abs" style="left:136px;top:70px;display:flex;align-items:center;gap:10px;font:700 24px/1 'Rubik',sans-serif;color:var(--yellow)"><i style="display:block;width:16px;height:16px;border-radius:50%;background:var(--yellow)"></i>Amber Kite Services</div>
  <div class="abs" style="left:136px;top:184px;font-size:11px;color:#bbbbbb">&copy; 2019 &nbsp;| &nbsp;Privacy Policy</div>
  <h5 style="left:456px;top:96px">QUICK LINKS</h5>
  <ul style="left:456px;top:122px"><li>Home</li><li>About Us</li><li>Services</li><li>Finance</li><li>Resource</li><li>Contact Us</li></ul>
  <h5 style="left:686px;top:96px">SERVICES</h5>
  <ul style="left:686px;top:122px"><li>Baseboard Heat Replacement</li><li>Ductless for Additions &amp; Remodels</li><li style="color:var(--yellow)">Ductless Installation</li><li>Ductless Maintenance</li><li>Ductless Repair</li></ul>
  <div class="social" style="left:955px;top:92px"><span></span><span></span><span></span><span></span></div>
</footer>

</body>
</html>
```